VELORAE is the product name. The product is a topical message oil for couples (his/her).

The package design needs to be erotic and classy. The design needs to carry over to the pump spray bottle. I already had a designed made for a similar product. I will include it as a sample but please do not copy it. Im looking for an original different design. However the oil, symbols are the same so use similar.
Requirements
Must have
- Only silver accents, no gold please. Thx

```html
<!DOCTYPE html>
<html lang="en">
<head>
<meta charset="utf-8">
<title>VELORAE – Sensual Massage Cream Packaging</title>
<link rel="stylesheet" href="https://fonts.googleapis.com/css2?family=Cinzel:wght@400&family=Roboto:wght@300;400;700&display=swap">
<style>
  :root {
    --canvas: #ffffff;
    --box-black: #050505;
    --photo-mid: #5a5a5a;
    --photo-dark: #1a1a1a;
    --label-white: #f1f1f1;
    --label-shade: #dcdcdc;
    --brand-red: #d8161e;
    --text-light: #e6e6e6;
    --text-dark: #2b2b2b;
    --chip-grey: #8a8a8a;
    --silver-dark: #3c3c3c;
    --silver-light: #f4f4f4;
    --icon-ring: #cfcfcf;
  }
  * { margin: 0; padding: 0; box-sizing: border-box; }
  html, body { width: 1200px; height: 900px; overflow: hidden; background: var(--canvas); }
  body { font-family: "Roboto", Arial, sans-serif; }

  .stage {
    width: 1200px; height: 900px;
    display: flex; align-items: center; justify-content: center; gap: 90px;
  }

  .silver-band {
    height: 12px; flex: none;
    background: linear-gradient(90deg, var(--silver-dark) 0%, var(--silver-light) 18%, #9a9a9a 40%, var(--silver-light) 62%, #7a7a7a 82%, var(--silver-dark) 100%);
  }

  .brand-name {
    font-family: "Cinzel", Georgia, serif;
    font-weight: 400;
    color: var(--brand-red);
    text-align: center;
    letter-spacing: 2px;
    white-space: nowrap;
  }

  .tagline { font-weight: 300; text-align: center; white-space: nowrap; }

  .audience-chip {
    position: absolute; left: 50%; transform: translateX(-50%);
    white-space: nowrap;
    background: var(--chip-grey);
    font-weight: 300; line-height: 1.25;
    color: #f4f4f4;
  }

  /* Box front panel */
  .box-front {
    width: 300px; height: 820px;
    background: var(--box-black);
    display: flex; flex-direction: column;
    color: var(--text-light);
  }
  .box-front .content { flex: 1; position: relative; }
  .box-front .brand-name { font-size: 40px; margin-top: 74px; }
  .box-front .couple-photo {
    position: absolute; left: 0; top: 152px; width: 100%; height: 332px;
    background:
      radial-gradient(ellipse 60% 45% at 35% 50%, var(--photo-mid), transparent 70%),
      radial-gradient(ellipse 45% 40% at 72% 52%, #6a6a6a, transparent 70%),
      linear-gradient(180deg, var(--box-black) 0%, var(--photo-dark) 30%, var(--photo-dark) 70%, var(--box-black) 100%);
  }
  .box-front .tagline { position: absolute; top: 520px; width: 100%; font-size: 23px; }
  .box-front .audience-chip {
    top: 554px; font-size: 16px; padding: 1px 9px;
    border: 1px solid #bdbdbd;
  }
  .infusion {
    position: absolute; top: 600px; width: 100%;
    text-align: center; font-size: 14px; font-weight: 300; white-space: nowrap;
  }
  .product-type {
    position: absolute; top: 624px; left: 34px; right: 34px;
    border-top: 1px solid #9a9a9a; border-bottom: 1px solid #9a9a9a;
    text-align: center; font-weight: 700; font-size: 16.5px; padding: 2px 0;
    letter-spacing: 0.3px; white-space: nowrap;
  }
  .claims {
    position: absolute; top: 668px; left: 38px; right: 38px;
    display: flex; justify-content: space-between;
  }
  .claim { width: 52px; text-align: center; }
  .claim svg { width: 36px; height: 36px; display: block; margin: 0 auto; }
  .claim span { display: block; font-size: 7px; margin-top: 6px; letter-spacing: 0.2px; white-space: nowrap; }
  .net-volume { position: absolute; top: 770px; width: 100%; text-align: center; font-size: 7px; }

  /* Bottle label */
  .bottle-label {
    width: 300px; height: 720px;
    background: linear-gradient(90deg, var(--label-shade) 0%, var(--label-white) 30%, #fafafa 55%, var(--label-shade) 100%);
    display: flex; flex-direction: column;
    color: var(--text-dark);
  }
  .bottle-label .content { flex: 1; position: relative; }
  .bottle-label .brand-name { font-size: 38px; margin-top: 64px; }
  .bottle-label .line-art {
    position: absolute; left: 40px; right: 40px; top: 140px; height: 300px;
    background: radial-gradient(ellipse 55% 50% at 55% 55%, #c9c9c9, transparent 72%);
  }
  .bottle-label .tagline { position: absolute; top: 470px; width: 100%; font-size: 25px; }
  .bottle-label .audience-chip {
    top: 508px; font-size: 15px; padding: 2px 12px; background: #8c8c8c;
  }
  .label-claim { position: absolute; top: 556px; width: 100%; text-align: center; }
  .label-claim svg { width: 40px; height: 40px; display: block; margin: 0 auto; }
  .label-claim span { display: block; font-size: 9px; font-weight: 700; margin-top: 4px; }
  .bottle-label .net-volume { top: 628px; font-size: 9px; }
</style>
</head>
<body>
<main class="stage">

  <section class="bottle-label" aria-label="Bottle label">
    <div class="silver-band"></div>
    <div class="content">
      <h2 class="brand-name">VELORAE</h2>
      <div class="line-art" role="img" aria-label="Fine line drawing of a couple about to kiss, with red lips"></div>
      <p class="tagline">Awaken Your Desire</p>
      <p class="audience-chip">FOR MEN AND WOMEN</p>
      <div class="label-claim">
        <svg viewBox="0 0 40 40" aria-hidden="true">
          <path d="M20 4 C26 14 32 20 32 27 A12 12 0 0 1 8 27 C8 20 14 14 20 4 Z" fill="none" stroke="#2b2b2b" stroke-width="1.6"/>
          <path d="M20 18 L20 33 M20 26 L14 21 M20 26 L26 21" stroke="#2b2b2b" stroke-width="1.4" fill="none" stroke-linecap="round"/>
        </svg>
        <span>HEMP OIL</span>
      </div>
      <p class="net-volume">NET 30ML</p>
    </div>
    <div class="silver-band"></div>
  </section>

  <section class="box-front" aria-label="Box front panel">
    <div class="silver-band"></div>
    <div class="content">
      <h1 class="brand-name">VELORAE</h1>
      <div class="couple-photo" role="img" aria-label="Black and white photograph of a couple about to kiss, woman with red lips"></div>
      <p class="tagline">Awaken Your Desire</p>
      <p class="audience-chip">FOR MEN AND WOMEN</p>
      <p class="infusion">CBD &amp; CBG INFUSED</p>
      <p class="product-type">SENSUAL MASSAGE CREAM</p>
      <div class="claims">
        <div class="claim">
          <svg viewBox="0 0 36 36" aria-hidden="true">
            <circle cx="18" cy="18" r="16" fill="#2a2a2a" stroke="var(--icon-ring)" stroke-width="2"/>
            <path d="M12 11 L18 26 L24 10" fill="none" stroke="#eee" stroke-width="1.8" stroke-linecap="round"/>
          </svg>
          <span>VEGAN</span>
        </div>
        <div class="claim">
          <svg viewBox="0 0 36 36" aria-hidden="true">
            <circle cx="18" cy="18" r="16" fill="#f2f2f2" stroke="var(--icon-ring)" stroke-width="2"/>
            <path d="M18 9 C21 14 24 17 24 21 A6 6 0 0 1 12 21 C12 17 15 14 18 9 Z" fill="#111"/>
          </svg>
          <span>PURE</span>
        </div>
        <div class="claim">
          <svg viewBox="0 0 36 36" aria-hidden="true">
            <circle cx="18" cy="18" r="16" fill="#f2f2f2" stroke="var(--icon-ring)" stroke-width="2"/>
            <path d="M18 25 C11 24 9 17 10 12 C15 12 18 16 18 25 Z M18 25 C25 24 27 17 26 12 C21 12 18 16 18 25 Z" fill="#111"/>
          </svg>
          <span>NATURAL</span>
        </div>
        <div class="claim">
          <svg viewBox="0 0 36 36" aria-hidden="true">
            <circle cx="18" cy="18" r="16" fill="#f2f2f2" stroke="var(--icon-ring)" stroke-width="2"/>
            <path d="M18 9 C21 14 24 17 24 21 A6 6 0 0 1 12 21 C12 17 15 14 18 9 Z" fill="#111"/>
            <path d="M18 17 L18 25 M18 21 L15.5 19 M18 21 L20.5 19" stroke="#f2f2f2" stroke-width="1.1" fill="none" stroke-linecap="round"/>
          </svg>
          <span>HEMP OIL</span>
        </div>
      </div>
      <p class="net-volume">NET 30ML</p>
    </div>
    <div class="silver-band"></div>
  </section>

</main>
</body>
</html>
```